business card for a shoe shop

we would like a business card for a family owned shoe shop.
With this information included.
Darnell's Shoe Store
Family owned since 1947

then on other side
Darnell's Shoe Store
Footwear fitting specialist
Phone: 9187 2630
218 Quarry St, Fernleigh Downs 3187
(cnr. Hartwick Rd and Quarry St)
darnellshoes218@examplemail.com
if could incorporate the purple color on card i have attached.

```html
<!DOCTYPE html>
<html lang="en">
<head>
<meta charset="utf-8">
<title>Darnell's Shoe Store – Business Card</title>
<link href="https://fonts.googleapis.com/css2?family=Montserrat:wght@400;800&family=Raleway:ital,wght@0,400;0,500;1,700&family=Roboto:wght@400&display=swap" rel="stylesheet">
<style>
  :root {
    --backdrop: #ddd6e3;
    --violet-deep: #5a2fd3;
    --violet: #7440ea;
    --violet-light: #9a5cf0;
    --paper: #ffffff;
    --paper-shade: #f1eff4;
    --ink: #1d1b22;
    --line-soft: #c9b8f2;
  }
  * { box-sizing: border-box; margin: 0; padding: 0; }
  html, body { width: 1200px; height: 800px; overflow: hidden; }
  body {
    background: var(--backdrop);
    display: flex;
    align-items: center;
    justify-content: center;
    gap: 60px;
    font-family: "Raleway", sans-serif;
  }
  .card {
    position: relative;
    width: 520px;
    height: 297px;
    border-radius: 42px;
    overflow: hidden;
  }

  /* Front */
  .card--front {
    background: linear-gradient(135deg, var(--violet) 0%, var(--violet-deep) 100%);
    color: var(--paper);
  }
  .card__frame { position: absolute; inset: 0; }
  .front__art {
    position: absolute;
    right: 40px;
    top: 22px;
    width: 120px;
    height: 120px;
    border-radius: 40%;
    background: radial-gradient(circle, rgba(255,255,255,0.22) 0%, rgba(255,255,255,0) 70%);
  }
  .brand { position: absolute; left: 54px; }
  .card--front .brand { top: 148px; }
  .brand__name {
    display: block;
    font-family: "Montserrat", sans-serif;
    font-weight: 800;
    font-size: 38px;
    line-height: 1;
    letter-spacing: 1px;
  }
  .brand__kind {
    display: block;
    font-family: "Montserrat", sans-serif;
    font-weight: 400;
    font-size: 33px;
    line-height: 1.1;
    letter-spacing: 1px;
  }
  .front__since {
    position: absolute;
    left: 230px;
    bottom: 28px;
    font-family: "Roboto", sans-serif;
    font-size: 17px;
    letter-spacing: 0.5px;
  }

  /* Back */
  .card--back {
    background: linear-gradient(180deg, var(--paper) 0%, var(--paper-shade) 100%);
    color: var(--ink);
  }
  .back__art {
    position: absolute;
    right: 34px;
    top: 16px;
    width: 160px;
    height: 150px;
    border-radius: 30%;
    background: radial-gradient(circle, rgba(201,184,242,0.45) 0%, rgba(201,184,242,0) 70%);
  }
  .back__line { position: absolute; inset: 0; }
  .card--back .brand { top: 40px; left: 34px; color: var(--violet-deep); }
  .card--back .brand__name { font-size: 27px; }
  .card--back .brand__kind { font-size: 24px; }
  .tagline {
    position: absolute;
    left: 34px;
    top: 118px;
    font-style: italic;
    font-weight: 700;
    font-size: 17px;
    color: var(--violet);
  }
  .contacts {
    position: absolute;
    left: 34px;
    top: 150px;
    list-style: none;
    font-weight: 500;
    font-size: 15px;
  }
  .contacts li { display: flex; align-items: center; gap: 10px; height: 24px; }
  .contacts svg { width: 18px; height: 18px; flex: none; }
  .address-band {
    position: absolute;
    left: 0; right: 0; bottom: 0;
    height: 72px;
    background: linear-gradient(90deg, var(--violet-light) 0%, var(--violet) 45%, var(--violet-deep) 100%);
    color: var(--paper);
    text-align: center;
    padding-top: 14px;
    font-size: 15px;
    line-height: 1.35;
    font-weight: 500;
    font-style: normal;
  }
</style>
</head>
<body>

  <section class="card card--front" aria-label="Card front">
    <svg class="card__frame" viewBox="0 0 520 297" fill="none" stroke="#ffffff" stroke-width="1.3" stroke-linejoin="round">
      <path d="M372 62 Q350 72 332 64 L292 34 L40 34 Q14 34 14 60 L14 256 Q14 282 40 282 L478 282 Q506 282 506 254 L506 102 Q506 84 490 78 L474 72"/>
    </svg>
    <div class="front__art" role="img" aria-label="Single-line drawing of a running shoe"></div>
    <h1 class="brand">
      <span class="brand__name">DARNELL'S</span>
      <span class="brand__kind">SHOE STORE</span>
    </h1>
    <p class="front__since">Family owned since 1947</p>
  </section>

  <section class="card card--back" aria-label="Card back">
    <div class="back__art" role="img" aria-label="Single-line drawing of a running shoe"></div>
    <svg class="back__line" viewBox="0 0 520 297" fill="none" stroke="var(--line-soft)" stroke-width="1.2">
      <path d="M240 56 Q260 50 290 62 Q310 70 330 64 L360 70"/>
    </svg>
    <h2 class="brand">
      <span class="brand__name">DARNELL'S</span>
      <span class="brand__kind">SHOE STORE</span>
    </h2>
    <p class="tagline">Footwear fitting specialist</p>
    <ul class="contacts">
      <li>
        <svg viewBox="0 0 24 24" fill="none" stroke="var(--ink)" stroke-width="1.6" stroke-linecap="round" stroke-linejoin="round" aria-hidden="true">
          <path d="M5 3h4l2 5-2.5 1.5a11 11 0 0 0 6 6L16 13l5 2v4a2 2 0 0 1-2 2A16 16 0 0 1 3 5a2 2 0 0 1 2-2z"/>
        </svg>
        <span>9187 2630</span>
      </li>
      <li>
        <svg viewBox="0 0 24 24" aria-hidden="true">
          <rect x="2" y="5" width="20" height="14" rx="1.5" fill="var(--ink)"/>
          <path d="M3 6l9 7 9-7" fill="none" stroke="#ffffff" stroke-width="1.6"/>
        </svg>
        <span>darnellshoes218@examplemail.com</span>
      </li>
    </ul>
    <address class="address-band">
      218 Quarry St, Fernleigh Downs 3187<br>
      (cnr. Hartwick Rd and Quarry St)
    </address>
  </section>

</body>
</html>
```